Lantern - Web Design Project

We are seeking to have our website redesigned. Our current webpage is rather dated looking www.lantern-outcomes.com We will be utilizing similar content to explain our services as what is in the website now. We do not see it at a retail portal but rather a website for those inquiring about our services as a reference check so to speak.

We wish to have a look that is considered clean, fresh, contemporary and contains a business savvy vibe.

We prefer isolated white background and also wish to retain the integrity of our Logo and colour scheme.

We are looking for something that doesnt look like it was designed at home on sitemoose. We are hoping to find something that looks like it would reside on a tablet.
Updates

Hello designers!

We apologize for our tardiness as we have been quite preoccupied. We will be extending our invites to the end of January!

Hello All,

Please review our offer once again for updated requirements.  We are hoping to accept a design by months end.

Lantern

Target Market(s)

Business to business clients and Large manufacturers

Industry/Entity Type

Retail

Requirements
Must have
• Existing Logo

There must be an area dedicated to an intro video that will be incorporated on our landing page.

We require design of the other pages as well not only the landing page.

```html
<!DOCTYPE html>
<html lang="en">
<head>
<meta charset="utf-8">
<title>Lantern Performance</title>
<link href="https://fonts.googleapis.com/css2?family=Bree+Serif&family=Ubuntu:ital,wght@0,400;0,500;1,400&family=Roboto+Condensed:wght@400;700&display=swap" rel="stylesheet">
<style>
:root{
  --red:#e01e1e;
  --ink:#333;
  --text:#555;
  --muted:#777;
  --line:#dcdcdc;
  --panel:#f4f4f4;
  --footer:#ececec;
  --black:#111;
}
*{margin:0;padding:0;box-sizing:border-box}
html,body{width:932px;height:1200px;overflow:hidden;background:#fff}
body{position:relative;font-family:"Ubuntu",sans-serif;color:var(--text)}
.abs{position:absolute}
.top-rule{left:0;top:0;width:932px;height:3px;background:var(--red)}
.signin{left:675px;top:0;width:75px;height:27px;background:var(--red);color:#fff;font-size:11px;line-height:28px;text-align:center;border-radius:0 0 0 14px}
.lang-bar{left:740px;top:0;width:192px;height:27px;background:var(--black);color:#fff;font-size:11px;line-height:27px;padding-left:14px;clip-path:polygon(0 0,100% 0,100% 100%,14px 100%)}
.brand{left:108px;top:34px;font-family:"Ubuntu",sans-serif;font-weight:500;font-size:34px;line-height:40px;color:#555;letter-spacing:-1px;display:flex;align-items:center;gap:8px}
.brand-dot{width:12px;height:12px;border-radius:50%;background:var(--red)}
.call-label{left:667px;top:44px;font-size:16px;color:#666}
.call-number{left:667px;top:60px;font-size:21px;color:var(--red);letter-spacing:.5px}
.nav{left:109px;top:103px;width:713px;height:31px;border:1px solid #d4d4d4;border-radius:16px;background:linear-gradient(#fff,#e9e9e9);display:flex;box-shadow:0 2px 3px rgba(0,0,0,.08)}
.nav a{font-family:"Roboto Condensed",sans-serif;font-size:11px;font-weight:700;color:#888;text-decoration:none;display:flex;align-items:center;justify-content:center;border-right:1px solid #d8d8d8;white-space:nowrap}
.nav a:last-child{border-right:0}
.nav a.current{color:#222}
.slider{left:109px;top:145px;width:713px;height:305px;border:1px solid #ddd;background:#f3f3f3;box-shadow:0 2px 4px rgba(0,0,0,.1)}
.slide-photo{left:116px;top:152px;width:699px;height:290px;background:linear-gradient(180deg,#5a3b78 0%,#b05a8a 30%,#3a2a3a 48%,#6d6f78 62%,#c9cbd2 100%)}
.caption{left:140px;top:373px;width:651px;height:47px;background:rgba(255,255,255,.82);font-family:"Ubuntu",sans-serif;font-style:italic;font-size:14.5px;color:#111;line-height:47px;padding-left:16px;white-space:nowrap;overflow:hidden;letter-spacing:-.1px}
.arrow{top:373px;width:24px;height:47px;background:var(--red)}
.welcome{left:109px;top:480px;width:713px;height:40px;display:flex;align-items:center;justify-content:center;gap:24px}
.welcome::before,.welcome::after{content:"";flex:1;height:5px;border-top:1px solid var(--line);border-bottom:1px solid var(--line)}
.welcome h1{font-family:"Bree Serif",serif;font-weight:400;font-size:25px;color:#444;white-space:nowrap}
.welcome h1 span{color:var(--red)}
.intro{left:128px;top:535px;width:676px;font-size:11.2px;line-height:16px;text-align:center;color:var(--text)}
.intro p+p{margin-top:16px}
.divider-shadow{left:40px;top:693px;width:852px;height:30px;background:radial-gradient(ellipse at top,rgba(0,0,0,.07),rgba(0,0,0,0) 70%)}
.section-title{font-family:"Bree Serif",serif;font-weight:400;font-size:18px;color:#222}
.quote{left:109px;top:773px;width:472px;height:116px;background:var(--panel);border:1px solid #e6e6e6;padding:20px 14px 20px 14px;font-size:10px;line-height:16px;color:#555}
.quote-tail{left:148px;top:888px}
.avatar{left:174px;top:900px;width:44px;height:44px;background:linear-gradient(#e9dcd3,#b89a88);border:2px solid #fff;outline:1px solid #ddd}
.author{left:230px;top:915px;font-size:11px;color:var(--red)}
.role{left:235px;top:933px;font-size:9.5px;color:#444}
.vrule{left:604px;top:735px;width:1px;height:210px;background:#eee}
.contact{left:630px;top:772px;font-size:10px;color:#222;line-height:13px}
.contact li{list-style:none;display:flex;gap:10px;margin-bottom:8px}
.contact svg{flex:none;margin-top:1px}
.map{left:628px;top:875px;width:173px;height:70px;background:linear-gradient(135deg,#dfe6d8,#c9d6e6);border:3px solid #ddd}
.footer{left:109px;top:1023px;width:713px;height:135px;background:var(--footer);border-radius:3px}
.footer h3{position:absolute;font-family:"Ubuntu",sans-serif;font-weight:400;font-size:13px;color:#333}
.footer ul{position:absolute;list-style:none;font-size:9.5px;color:#666;line-height:17.5px}
.social li{display:flex;align-items:center;gap:10px;line-height:19px}
.social i{width:11px;height:11px;background:#4a6ea9;display:block}
.news-text{left:492px;top:47px;width:170px;font-size:9.5px;line-height:13px;color:#666}
.email{left:492px;top:84px;width:155px;height:26px;background:#fff;border:1px solid #ddd;font-size:9.5px;color:#555;line-height:24px;padding-left:6px}
.submit{left:646px;top:84px;width:50px;height:26px;background:var(--red);color:#fff;font-size:10px;font-weight:500;line-height:26px;text-align:center}
.copyright{left:0;top:1171px;width:932px;text-align:center;font-size:9px;color:#888}
</style>
</head>
<body>
<div class="abs top-rule"></div>
<div class="abs signin">Sign In</div>
<div class="abs lang-bar">Language &#9678;</div>

<div class="abs brand"><span class="brand-dot"></span>Lantern</div>
<div class="abs call-label">Questions? Call</div>
<div class="abs call-number">1.877.555.0142</div>

<nav class="abs nav">
  <a class="current" style="width:87px">HOME</a>
  <a style="width:100px">WHO WE ARE</a>
  <a style="width:130px">CROSS THE LANTERN</a>
  <a style="width:165px">PERFORMANCE SOLUTIONS</a>
  <a style="width:135px">SUSTAIN SOLUTIONS</a>
  <a style="width:94px">JOIN US</a>
</nav>

<div class="abs slider"></div>
<div class="abs slide-photo" role="img" aria-label="Lit pedestrian bridge at dusk under a purple sky"></div>
<div class="abs caption">"Neque porro quisquam est qui dolorem ipsum quia dolor sit amet, consectetur, adipisci velit..."</div>
<div class="abs arrow" style="left:116px"><svg width="24" height="47"><path d="M15 14 L9 23.5 L15 33" stroke="#fff" stroke-width="1.6" fill="none"/></svg></div>
<div class="abs arrow" style="left:791px"><svg width="24" height="47"><path d="M9 14 L15 23.5 L9 33" stroke="#fff" stroke-width="1.6" fill="none"/></svg></div>

<div class="abs welcome"><h1>Welcome to <span>Lantern Performance</span></h1></div>
<div class="abs intro">
  <p>Lorem Ipsum is simply dummy text of the printing and typesetting industry. Lorem Ipsum has been the industry's standard dummy text ever since the 1500s.When an unknown printer took a galley of type and scrambled it to make a type specimen book.Lorem Ipsum is simply dummy text of the printing and typesetting industry. Lorem Ipsum has been the industry's standard dummy text ever since the 1500s.</p>
  <p>When an unknown printer took a galley of type and scrambled it to make a type specimen book.It has survived not only five centuries, but also the leap into electronic typesetting, remaining essentially unchanged.</p>
</div>
<div class="abs divider-shadow"></div>

<h2 class="abs section-title" style="left:109px;top:737px">Client's Speak</h2>
<div class="abs quote">"Lorem Ipsum is simply dummy text of the printing and typesetting industry. Lorem Ipsum has been the industry's standard dummy text ever since the 1500s.When an unknown printer took a galley of type and scrambled it to make a type specimen book.Lorem Ipsum is simply dummy text of the printing and typesetting industry. Lorem Ipsum has been the industry's standard dummy text ever since the 1500s.</div>
<svg class="abs quote-tail" width="24" height="14"><path d="M0 0 L22 0 L12 13 Z" fill="#f4f4f4"/><path d="M0 0 L12 13 L22 0" stroke="#e6e6e6" fill="none"/></svg>
<div class="abs avatar" role="img" aria-label="Client portrait"></div>
<div class="abs author">- Celia Marwood</div>
<div class="abs role">Chief Executive (Lorem ipsum amet...)</div>

<div class="abs vrule"></div>
<h2 class="abs section-title" style="left:628px;top:737px">Contact Info</h2>
<ul class="abs contact">
  <li><svg width="10" height="13"><path d="M5 0a4.5 4.5 0 0 1 4.5 4.5C9.5 8 5 13 5 13S.5 8 .5 4.5A4.5 4.5 0 0 1 5 0z" fill="#e01e1e"/><circle cx="5" cy="4.5" r="1.6" fill="#fff"/></svg><span>48 Harbourview Rd, Kingsford,<br>ON K2X 4P8, Canada</span></li>
  <li style="margin-top:2px"><svg width="12" height="12"><path d="M2 1 L5 1 L6 4 L4.5 5.5 C5.5 7.5 6.5 8.5 8.5 9.5 L10 8 L12 9 L12 12 C6 12 0 6 1 1 Z" fill="#e01e1e"/></svg><span>Phone: +1.877.555.0142</span></li>
  <li><svg width="12" height="12"><rect x="0" y="2" width="12" height="8" fill="#e01e1e"/><path d="M0 2 L6 7 L12 2" stroke="#fff" fill="none"/></svg><span>Email:info@lantern-outcomes.com</span></li>
  <li><svg width="12" height="12"><circle cx="6" cy="3.5" r="3" fill="#e01e1e"/><path d="M0 12 C0 7 12 7 12 12 Z" fill="#e01e1e"/></svg><span>Everyday: 07:00AM to 05:00PM</span></li>
</ul>
<div class="abs map" role="img" aria-label="Map of the office location"></div>

<footer class="abs footer">
  <h3 style="left:15px;top:22px">Quick Links</h3>
  <ul style="left:15px;top:44px"><li>Home</li><li>Who We Are</li><li>Cross The Lantern</li></ul>
  <ul style="left:141px;top:44px"><li>Performance Solutions</li><li>Sustain Solutions</li><li>Join Us</li></ul>
  <h3 style="left:313px;top:22px">Get In Touch</h3>
  <ul class="social" style="left:313px;top:44px"><li><i></i>Circlepage</li><li><i style="background:#3aa9d8"></i>Chirpline</li><li><i style="background:#2a79b2"></i>Worknet</li></ul>
  <h3 style="left:492px;top:22px">Sign Up For Our Newsletter</h3>
  <div class="abs news-text">Sign up to receive special offers and promotions.</div>
  <div class="abs email">Enter your email address</div>
  <div class="abs submit">SUBMIT</div>
</footer>
<div class="abs copyright">Copyright &copy; 2012 Lantern Performance. All Rights Reserved.</div>
</body>
</html>
```